Morvik Construction Business Card

I need a business card design for my company.
We are a construction/machinery company.
I would like to see my logo on the front of the card and my details on the other side
I would like the card to be black or dark grey in colour,with my logo as i send it or modified with a lighter blue colour
I would like to see the design kept fairly simple,but eye catching at the same time
Industry/Entity Type
Business
Colors
00a990
1b1b1b
000000
474747
ececec

```html
<!DOCTYPE html>
<html lang="en">
<head>
<meta charset="utf-8">
<title>Morvik Construction Business Card</title>
<link rel="stylesheet" href="https://fonts.googleapis.com/css2?family=Open+Sans:wght@400;600;700;800&display=swap">
<style>
  :root {
    --teal: #00a990;
    --ink: #1b1b1b;
    --black: #000000;
    --graphite: #474747;
    --paper: #ececec;
    --white: #ffffff;
    --backdrop: #d9d6d0;
  }
  * { box-sizing: border-box; margin: 0; padding: 0; }
  html, body {
    width: 1200px;
    height: 780px;
    overflow: hidden;
    background: var(--backdrop);
    font-family: "Open Sans", Arial, sans-serif;
  }
  .stage {
    width: 1200px;
    height: 780px;
    display: flex;
    align-items: center;
    justify-content: center;
    gap: 90px;
  }
  .card {
    position: relative;
    width: 380px;
    height: 650px;
    border-radius: 26px;
    overflow: hidden;
    box-shadow: 0 14px 30px rgba(0,0,0,0.25);
  }

  /* Front: details side */
  .card--front { background: var(--ink); }
  .card--front .card__bands {
    position: absolute;
    inset: 0;
    width: 100%;
    height: 100%;
  }
  .brand {
    position: absolute;
    top: 92px;
    left: 0;
    right: 0;
    display: flex;
    align-items: center;
    justify-content: center;
    gap: 14px;
  }
  .brand__square {
    width: 26px;
    height: 26px;
    background: var(--black);
    flex: none;
  }
  .brand__name {
    color: var(--black);
    font-weight: 800;
    font-size: 25px;
    letter-spacing: 1px;
    line-height: 1.15;
    text-transform: uppercase;
  }
  .details {
    position: absolute;
    top: 380px;
    left: 0;
    right: 0;
    text-align: center;
    color: var(--white);
  }
  .details__name {
    font-weight: 700;
    font-size: 27px;
    letter-spacing: 1px;
    text-transform: uppercase;
  }
  .details__role {
    font-weight: 600;
    font-size: 20px;
    margin-top: 2px;
    margin-bottom: 26px;
  }
  .details__line {
    font-size: 19px;
    font-weight: 600;
    line-height: 1.4;
  }

  /* Back: logo side */
  .card--back {
    background: linear-gradient(160deg, #2a2a2a 0%, var(--ink) 45%, var(--black) 100%);
  }
  .wordmark {
    position: absolute;
    top: 50%;
    left: 50%;
    transform: translate(-50%, -50%) rotate(90deg);
    white-space: nowrap;
    color: var(--white);
    font-weight: 800;
    font-size: 46px;
    letter-spacing: 3px;
    line-height: 1.1;
    text-transform: uppercase;
    text-align: left;
  }
</style>
</head>
<body>
<main class="stage">
  <section class="card card--front" aria-label="Card front with contact details">
    <svg class="card__bands" viewBox="0 0 380 650" preserveAspectRatio="none" aria-hidden="true">
      <rect width="380" height="650" fill="var(--ink)"/>
      <path d="M0 0 H380 V330 Q200 360 0 230 Z" fill="var(--teal)"/>
      <path d="M0 0 H380 V312 Q200 345 0 212 Z" fill="var(--white)"/>
    </svg>
    <div class="brand">
      <span class="brand__square"></span>
      <span class="brand__name">Morvik<br>Construction</span>
    </div>
    <div class="details">
      <p class="details__name">Employee Name</p>
      <p class="details__role">Managing Director</p>
      <p class="details__line">000-111-0000</p>
      <p class="details__line">abc@youremail.com</p>
      <p class="details__line">0000 your address Avenue</p>
      <p class="details__line">Kestrel Falls, ND 0000</p>
    </div>
  </section>

  <section class="card card--back" aria-label="Card back with company name">
    <p class="wordmark">Morvik<br>Construction</p>
  </section>
</main>
</body>
</html>
```